Building company with a modern and unique product looking for a business card to help us stand out

We currently have a logo but as our business has grown, we feel that our business card is not reflecting our modern and high quality product and help us stand out from the crowd. Our business is mainly in the construction of new homes using a unique method and materials that makes our homes fire proof, vermin and pest resistant and rated to the maximum cyclone category (category 5). We need a business card that helps us stand out as well as communicating professionalism, high quality and trustworthiness. I have attached our current logo with a black and white option, as well as our business card which is double sided. We would like to retain as much of the information that is currently on our business cards, but presented in a more sleek way. We do like our current colour palette ( white, black, yellow and grey) and have been looking primarily at business cards with a black background however we are open to other combinations of colour and layout as long as we stand out. Please feel free to tweak our logo to make it more suitable for a business card, we like the black option that we use but we have had trouble trying to get the white area to match the rest of the logo and blend effectively into a business card. Please do not hesitate to contact us with any questions as we really want this to be successful!

Target Market(s)

Large contracts including government and larger companies

Industry/Entity Type

Business

We will be providing this business card to potential clients including key government ministers and large funding companies, our business card should show that we are professional and reliable.

Requirements
Must have
• It must be easy to read and pleasing to the eye, It must contain as much of the information on the current business card and unless something really stands out, we will most likely pick a design that has all of the information included. It must include our logo of course and have some colour included.
Nice to have
• We are looking for a high end business card and would like to see designs that reflect this. We like the gloss/matte contrast, plastic cards with opaque/coloured areas and unique features not seen on everyday paper business cards. It would be nice to see a few different colour combinations, we are open to new ideas so please feel free to take some artistic licence.
Should not have
• Must not be too busy, difficult to read or be distracting from the information conveyed. Other than this please feel free to add your own touches and make it unique!

```html
<!DOCTYPE html>
<html lang="en">
<head>
<meta charset="utf-8">
<title>Ridgeline Building Company – Business Cards</title>
<link href="https://fonts.googleapis.com/css2?family=Open+Sans:wght@400;600;700&display=swap" rel="stylesheet">
<style>
  :root {
    --backdrop: #d4d4d4;
    --card: #ffffff;
    --ink: #1a1a1a;
    --band: #262626;
    --accent: #f2e21a;
    --muted: #555555;
    --rule: #9a9a9a;
  }
  * { box-sizing: border-box; margin: 0; padding: 0; }
  html, body {
    width: 1200px; height: 900px; overflow: hidden;
    background: var(--backdrop);
    font-family: "Open Sans", Arial, sans-serif;
    color: var(--ink);
  }
  .sheet {
    width: 1200px; height: 900px;
    display: flex; flex-direction: column; align-items: center; justify-content: center;
    gap: 50px;
  }
  .card {
    position: relative;
    width: 660px; height: 378px;
    background: var(--card);
    box-shadow: 0 6px 18px rgba(0,0,0,0.18);
    overflow: hidden;
  }

  /* Brand lockup shared by both sides */
  .brand { display: flex; align-items: center; gap: 10px; }
  .brand-mark { width: 16px; height: 16px; background: var(--accent); flex: none; }
  .brand-name {
    font-weight: 700; color: var(--ink); line-height: 1.15;
  }

  /* Contact side */
  .card--contact .edge {
    position: absolute; width: 22px; background: var(--band);
  }
  .card--contact .edge--left { left: 0; top: 150px; height: 110px; }
  .card--contact .edge--right { right: 0; top: 0; height: 90px; }
  .contact-layout {
    position: absolute; left: 60px; top: 70px; right: 60px;
    display: flex; align-items: center;
  }
  .card--contact .brand-name { font-size: 24px; width: 190px; }
  .divider {
    width: 1px; height: 96px; background: var(--rule); margin: 0 26px;
  }
  .person-name { font-size: 20px; font-weight: 700; }
  .person-role { font-size: 12px; color: var(--muted); margin-bottom: 8px; }
  .contact-list { list-style: none; font-size: 15px; line-height: 1.6; }
  .contact-list li { display: flex; align-items: center; gap: 8px; }
  .contact-list svg { width: 14px; height: 14px; flex: none; }
  .specialties {
    position: absolute; left: 60px; right: 40px; top: 236px;
    font-size: 17px;
  }
  .specialties-title { margin-bottom: 6px; }
  .specialty-list { list-style: none; display: flex; gap: 18px; flex-wrap: wrap; }
  .specialty-list li { display: flex; align-items: center; gap: 6px; }
  .tick { width: 15px; height: 15px; flex: none; }

  /* Brand side */
  .card--brand .top-band {
    position: absolute; left: 0; top: 0; width: 100%; height: 150px;
    background: var(--band);
  }
  .card--brand .brand {
    position: absolute; right: 48px; top: 172px;
    align-items: flex-start;
  }
  .card--brand .brand-mark { margin-top: 11px; }
  .card--brand .brand-name { font-size: 30px; }
  .card--brand .brand-sub { display: block; }
</style>
</head>
<body>
<main class="sheet">

  <section class="card card--contact" aria-label="Business card, contact side">
    <div class="edge edge--left"></div>
    <div class="edge edge--right"></div>

    <div class="contact-layout">
      <div class="brand">
        <span class="brand-mark"></span>
        <span class="brand-name">Ridgeline Building Company</span>
      </div>
      <div class="divider"></div>
      <div class="person">
        <p class="person-name">Callum Reeves</p>
        <p class="person-role">Managing Director</p>
        <ul class="contact-list">
          <li>
            <svg viewBox="0 0 14 14" aria-hidden="true"><rect x="3" y="0.5" width="8" height="13" rx="1.5" fill="var(--ink)"/><rect x="4.5" y="2" width="5" height="8" fill="#fff"/></svg>
            : 0400 123 456
          </li>
          <li>
            <svg viewBox="0 0 14 14" aria-hidden="true"><path d="M3 1 L5.5 3.5 L4 5.5 C5 8 6 9 8.5 10 L10.5 8.5 L13 11 L11 13 C5 12.5 1.5 9 1 3 Z" fill="var(--ink)"/></svg>
            : (02) 5550 1234
          </li>
          <li>
            <svg viewBox="0 0 14 14" aria-hidden="true"><rect x="0.5" y="2.5" width="13" height="9" fill="var(--ink)"/><path d="M1 3 L7 8 L13 3" stroke="#fff" stroke-width="1.2" fill="none"/></svg>
            : hello@ridgelinebuild.com
          </li>
        </ul>
      </div>
    </div>

    <div class="specialties">
      <p class="specialties-title">Specializing in Homes that are</p>
      <ul class="specialty-list">
        <li><svg class="tick" viewBox="0 0 15 15" aria-hidden="true"><rect width="15" height="15" fill="var(--ink)"/><path d="M3 8 L6 11 L12 4" stroke="var(--accent)" stroke-width="2" fill="none"/></svg>Fire Proof</li>
        <li><svg class="tick" viewBox="0 0 15 15" aria-hidden="true"><rect width="15" height="15" fill="var(--ink)"/><path d="M3 8 L6 11 L12 4" stroke="var(--accent)" stroke-width="2" fill="none"/></svg>Climate Proof</li>
        <li><svg class="tick" viewBox="0 0 15 15" aria-hidden="true"><rect width="15" height="15" fill="var(--ink)"/><path d="M3 8 L6 11 L12 4" stroke="var(--accent)" stroke-width="2" fill="none"/></svg>Cyclone Rated (Cat. 5)</li>
      </ul>
    </div>
  </section>

  <section class="card card--brand" aria-label="Business card, brand side">
    <div class="top-band"></div>
    <div class="brand">
      <span class="brand-mark"></span>
      <span class="brand-name">Ridgeline Building<span class="brand-sub">Company</span></span>
    </div>
  </section>

</main>
</body>
</html>
```